SHG business cards

design a business card

(Generators . Lighting Towers . De-watering Pumps . Compressors) put under the logo please. my details are Marek Oyelaran (Director) 0461527308 silverpinehaulgroup@postvane.com

```html
<!DOCTYPE html>
<html lang="en">
<head>
<meta charset="UTF-8">
<title>SHG Business Cards</title>
<link href="https://fonts.googleapis.com/css2?family=Montserrat:wght@400;500;700;800&display=swap" rel="stylesheet">
<style>
  :root {
    --backdrop: #2b2b2b;
    --amber: #e09d3a;
    --amber-deep: #d88f2c;
    --card-black: #1a1a1a;
    --silver: #b4b4b4;
    --silver-light: #cfcfcf;
    --white: #ffffff;
    --text-light: #e8e8e8;
  }
  * { margin: 0; padding: 0; box-sizing: border-box; }
  html, body {
    width: 1200px; height: 875px; overflow: hidden;
    background: var(--backdrop);
    font-family: "Montserrat", sans-serif;
  }
  .canvas {
    position: relative; width: 1200px; height: 875px;
    display: flex; align-items: center; justify-content: center; gap: 40px;
  }
  .card {
    position: relative; width: 540px; height: 310px;
    border-radius: 18px; overflow: hidden;
    box-shadow: 0 18px 40px rgba(0,0,0,0.45);
  }

  /* Front */
  .card-front {
    background: var(--amber);
    display: flex; flex-direction: column; align-items: center; justify-content: center;
  }
  .brand-lockup { display: flex; align-items: center; gap: 14px; }
  .brand-mark { width: 30px; height: 30px; background: var(--silver-light); }
  .brand-name {
    font-weight: 800; color: var(--silver-light);
    font-size: 30px; letter-spacing: 1px; line-height: 1.1; text-transform: uppercase;
  }
  .brand-rule { width: 380px; height: 1px; background: var(--silver-light); margin: 14px 0 16px; }
  .services {
    font-weight: 700; font-size: 13.5px; color: var(--white); letter-spacing: 0.2px;
  }

  /* Back */
  .card-back { background: var(--card-black); }
  .card-back .edge-bands { position: absolute; inset: 0; }
  .back-content {
    position: absolute; inset: 0;
    display: flex; align-items: center; padding: 0 36px;
  }
  .back-brand { width: 200px; display: flex; flex-direction: column; align-items: flex-start; gap: 8px; }
  .back-brand .brand-lockup { gap: 10px; }
  .back-brand .brand-mark { width: 18px; height: 18px; background: var(--amber); }
  .back-brand .brand-name { color: var(--amber); font-size: 17px; letter-spacing: 0.5px; }
  .divider { width: 1.5px; height: 120px; background: var(--amber); margin: 0 22px; }
  .contact { color: var(--text-light); }
  .contact-name { font-weight: 700; font-size: 22px; color: var(--amber); }
  .contact-role { font-size: 13px; margin: 2px 0 12px; }
  .contact-list { list-style: none; font-size: 11.5px; display: flex; flex-direction: column; gap: 6px; }
  .contact-list li { display: flex; align-items: center; gap: 8px; }
  .contact-list svg { width: 11px; height: 11px; flex: none; fill: var(--amber); }
</style>
</head>
<body>
<main class="canvas">

  <section class="card card-front">
    <div class="brand-lockup">
      <span class="brand-mark"></span>
      <span class="brand-name">Silver Pine<br>Haul Group</span>
    </div>
    <div class="brand-rule"></div>
    <p class="services">Generators . Lighting Towers . De-watering Pumps . Compressors</p>
  </section>

  <section class="card card-back">
    <svg class="edge-bands" viewBox="0 0 540 310" preserveAspectRatio="none">
      <polygon points="0,0 215,0 200,20 0,20" fill="var(--amber-deep)"/>
      <polygon points="222,0 540,0 540,10 215,10" fill="var(--silver)"/>
      <polygon points="0,290 340,290 355,310 0,310" fill="var(--amber-deep)"/>
      <polygon points="345,294 540,294 540,310 358,310" fill="var(--silver)"/>
    </svg>
    <div class="back-content">
      <div class="back-brand">
        <div class="brand-lockup">
          <span class="brand-mark"></span>
          <span class="brand-name">Silver Pine<br>Haul Group</span>
        </div>
      </div>
      <div class="divider"></div>
      <div class="contact">
        <h1 class="contact-name">Marek Oyelaran</h1>
        <p class="contact-role">Director</p>
        <ul class="contact-list">
          <li>
            <svg viewBox="0 0 24 24"><path d="M6.6 10.8a15.1 15.1 0 0 0 6.6 6.6l2.2-2.2a1 1 0 0 1 1-.25 11.4 11.4 0 0 0 3.6.57 1 1 0 0 1 1 1V20a1 1 0 0 1-1 1A17 17 0 0 1 3 4a1 1 0 0 1 1-1h3.5a1 1 0 0 1 1 1c0 1.25.2 2.46.57 3.6a1 1 0 0 1-.25 1z"/></svg>
            0461527308
          </li>
          <li>
            <svg viewBox="0 0 24 24"><path d="M2 5h20v14H2zM4 7v.5l8 5 8-5V7l-8 5z"/></svg>
            silverpinehaulgroup@postvane.com
          </li>
          <li>
            <svg viewBox="0 0 24 24"><path d="M12 2a10 10 0 1 0 0 20 10 10 0 0 0 0-20zm6.9 6h-3a15.6 15.6 0 0 0-1.3-4A8 8 0 0 1 18.9 8zM12 4c.8 1.2 1.5 2.5 1.9 4h-3.8c.4-1.5 1.1-2.8 1.9-4zM4.3 14a8 8 0 0 1 0-4h3.4a16 16 0 0 0 0 4zm.8 2h3a15.6 15.6 0 0 0 1.3 4A8 8 0 0 1 5.1 16zm3-8h-3a8 8 0 0 1 4.3-4 15.6 15.6 0 0 0-1.3 4zM12 20c-.8-1.2-1.5-2.5-1.9-4h3.8c-.4 1.5-1.1 2.8-1.9 4zm2.3-6H9.7a14.7 14.7 0 0 1 0-4h4.6a14.7 14.7 0 0 1 0 4zm.3 6a15.6 15.6 0 0 0 1.3-4h3a8 8 0 0 1-4.3 4zm1.7-6a16 16 0 0 0 0-4h3.4a8 8 0 0 1 0 4z"/></svg>
            silverpinehaulgroup.com
          </li>
        </ul>
      </div>
    </div>
  </section>

</main>
</body>
</html>
```